Sleep/Snoring Business - Requires Website - Australia

We are seeking a simple to maintain website for our sleep business. The health care business provides diagnostic and treatment solutions for snoring, sleep disorders and other respiratory problems.

Ideally, colours to match the company logo (attached).

The page must be built using WORDPRESS.

Ideally site will have a home page outlining the business, with 5 sub pages - being "Diagnosis" "Treatment Options", "Prodcuts", "About Us", "Contact Us"

The site home page should include a large picture on the home page.

The "Treatment Options" and "Diagnosis" pages must include:
Allow for a few pictures with assocaited text, plus space for some embeded youtube videos.

"Prodcuts" page should have the ability to show 3-4 products across the page with text below.. that can include external URL to products

The "About Us" page must include:
1. a Map (google map) to identify the various locations. There are 6 in total.
2. A Section to describe our doctors/staff - allow for a picture and some text

The "Contact Us" page must include:
email form
telephone details

The overall design should have a clean and medical/safe feeling

People who snore and those with sleeping and respiratory disorders

Health Care

• The page must be built using WORDPRESS.
• Ideally site will have a home page outlining the business, with 5 sub pages - being "Diagnosis" "Treatment Options", "Prodcuts", "About Us", "Contact Us"
• The site home page should include a large picture on the home page.
• The "Treatment Options" and "Diagnosis" pages must include:
• Allow for a few pictures with assocaited text, plus space for some embeded youtube videos.
• "Prodcuts" page should have the ability to show 3-4 products across the page with text below.. that can include external URL to products
• The "About Us" page must include:
• 1. a Map (google map) to identify the various locations. There are 6 in total.
• 2. A Section to describe our doctors/staff - allow for a picture and some text
• The "Contact Us" page must include:
• email form
• telephone details
• Pictures must be licenced or free to use
• Home page pictures showing people sleeping well, snoring or fresh air (landscape) type transition pictures (at least 3).
• Not to look cheap
• This is a high end healthcare business, so must look that way

```html
<!DOCTYPE html>
<html lang="en">
<head>
<meta charset="utf-8">
<title>Restwell Clinics</title>
<link rel="stylesheet" href="https://fonts.googleapis.com/css2?family=Lato:wght@400;700&family=Cabin:wght@500&display=swap">
<style>
:root{
  --navy:#114b7e;
  --navy-text:#1d4f83;
  --sky:#8fadd6;
  --ring:#9db5da;
  --ink:#2b2b2b;
  --white:#ffffff;
  --rule:#d9dfe8;
}
*{margin:0;padding:0;box-sizing:border-box}
html,body{width:1200px;height:894px;overflow:hidden;background:var(--white)}
body{font-family:"Lato",sans-serif;color:var(--ink);position:relative}
.page{position:relative;width:1200px;height:894px;overflow:hidden}

/* header */
.site-header{position:absolute;top:0;left:0;width:1200px;height:143px;background:var(--white);border-bottom:1px solid var(--rule);z-index:3}
.brand{position:absolute;left:52px;top:48px;display:flex;align-items:center;gap:10px;font-family:"Lato",sans-serif;font-weight:700;font-size:34px;color:var(--navy);letter-spacing:-0.5px}
.brand-dot{width:22px;height:22px;border-radius:50%;background:var(--navy)}
.social{position:absolute;display:flex;gap:13px}
.social span{display:block;border-radius:50%}
.header-social{left:810px;top:23px}
.header-social span{width:33px;height:33px;border:1.5px solid var(--ring)}
.header-divider{position:absolute;left:964px;top:23px;width:1px;height:35px;background:var(--rule)}
.header-phone{position:absolute;left:990px;top:23px;display:flex;align-items:center;gap:10px;font-weight:700;font-size:17px;color:#3a3a3a;letter-spacing:0.3px}
.icon-ring{width:33px;height:33px;border-radius:50%;border:1.5px solid var(--ring);display:flex;align-items:center;justify-content:center}
.main-nav{position:absolute;right:52px;top:96px;display:flex;align-items:center}
.main-nav a{position:relative;display:block;padding:0 26px;font-size:17px;color:#333;text-decoration:none;line-height:22px;border-left:1px solid var(--rule)}
.main-nav a:first-child{border-left:none}
.main-nav a:last-child{padding-right:0}
.main-nav a.is-active{color:var(--navy-text)}
.main-nav a.is-active::before{content:"";position:absolute;left:50%;top:-16px;width:34px;height:10px;margin-left:-23px;border-bottom:3px solid #c5d4ea;border-radius:0 0 50% 50%}

/* hero */
.hero{position:absolute;top:143px;left:0;width:1200px;height:620px;
  background:
    radial-gradient(ellipse 320px 300px at 870px 290px,#f1d2b0 0%,#e8c29a 40%,rgba(232,194,154,0) 72%),
    radial-gradient(ellipse 300px 260px at 1080px 150px,#ecd3a0 0%,rgba(236,211,160,0) 70%),
    linear-gradient(100deg,#dfe6ee 0%,#e9eef4 45%,#f4f6f9 62%,#eef2f6 100%)}
.hero-copy{position:absolute;left:52px;top:178px;font-family:"Cabin",sans-serif;font-weight:500;font-size:32px;line-height:45.5px;color:#111}
.hero-dots{position:absolute;left:52px;top:360px;display:flex;gap:10px}
.hero-dots span{width:15px;height:15px;border-radius:50%;background:var(--white)}
.hero-dots span.is-current{background:var(--navy);border:2px solid var(--white)}
.hero-curve{position:absolute;left:0;top:560px;width:1200px;height:200px;z-index:2}

/* footer */
.site-footer{position:absolute;left:0;top:740px;width:1200px;height:154px;background:var(--navy);color:var(--white);z-index:2}
.footer-nav{position:absolute;left:53px;top:21px;display:flex}
.footer-nav a{display:block;padding:0 23px;font-size:15px;color:var(--white);text-decoration:none;line-height:20px;border-left:1px solid rgba(255,255,255,0.35)}
.footer-nav a:first-child{padding-left:0;border-left:none}
.footer-social{right:52px;top:9px;left:auto}
.footer-social span{width:34px;height:34px;border:1.5px solid var(--white)}
.footer-rule{position:absolute;left:0;top:66px;width:1200px;height:1px;background:rgba(255,255,255,0.3)}
.contact-item{position:absolute;top:90px;display:flex;gap:12px;font-size:15px;line-height:25px}
.contact-item strong{display:block;font-weight:700}
.contact-icon{width:34px;height:34px;border-radius:50%;background:var(--sky);display:flex;align-items:center;justify-content:center;flex:none;margin-top:1px}
.contact-address{left:53px}
.contact-call{left:400px}
.contact-email{left:589px}
.contact-email .value{font-size:16px;letter-spacing:0.6px}
.copyright{position:absolute;right:53px;top:100px;text-align:center;font-size:14px;line-height:20px}
</style>
</head>
<body>
<div class="page">

  <header class="site-header">
    <div class="brand"><span class="brand-dot"></span>Restwell Clinics</div>
    <div class="social header-social" aria-label="Social links"><span></span><span></span><span></span></div>
    <div class="header-divider"></div>
    <div class="header-phone">
      <span class="icon-ring">
        <svg width="18" height="18" viewBox="0 0 24 24"><path fill="#9db5da" d="M6.6 10.8c1.4 2.8 3.8 5.1 6.6 6.6l2.2-2.2c.3-.3.7-.4 1-.2 1.1.4 2.3.6 3.6.6.6 0 1 .4 1 1V20c0 .6-.4 1-1 1C10.6 21 3 13.4 3 4c0-.6.4-1 1-1h3.5c.6 0 1 .4 1 1 0 1.3.2 2.5.6 3.6.1.3 0 .7-.2 1z"/></svg>
      </span>
      015-550-0142
    </div>
    <nav class="main-nav">
      <a href="#" class="is-active">Home</a>
      <a href="#">Diagnosis</a>
      <a href="#">Treatment</a>
      <a href="#">Products</a>
      <a href="#">About Us</a>
      <a href="#">Contact Us</a>
    </nav>
  </header>

  <section class="hero" role="img" aria-label="Woman sleeping peacefully on white pillows under a white duvet">
    <h1 class="hero-copy">We Provide Diagnostic and Treatment<br>Solutions For Snoring, Sleep Disorders<br>And Other Respiratory Problems</h1>
    <div class="hero-dots"><span class="is-current"></span><span></span><span></span><span></span></div>
  </section>

  <svg class="hero-curve" viewBox="0 0 1200 200" preserveAspectRatio="none" aria-hidden="true">
    <path d="M0,52 Q600,256 1200,2 L1200,200 L0,200 Z" fill="#ffffff"/>
    <path d="M0,55 Q600,262 1200,6 L1200,200 L0,200 Z" fill="#8fadd6"/>
    <path d="M0,62 Q620,272 1200,50 L1200,200 L0,200 Z" fill="#114b7e"/>
  </svg>

  <footer class="site-footer">
    <nav class="footer-nav">
      <a href="#">Home</a>
      <a href="#">Diagnosis</a>
      <a href="#">Treatment</a>
      <a href="#">Products</a>
      <a href="#">About Us</a>
      <a href="#">Contact Us</a>
    </nav>
    <div class="social footer-social" aria-label="Social links"><span></span><span></span><span></span></div>
    <div class="footer-rule"></div>

    <div class="contact-item contact-address" style="top:88px">
      <span class="contact-icon">
        <svg width="16" height="18" viewBox="0 0 24 24"><path fill="#fff" d="M12 2C8.1 2 5 5.1 5 9c0 5.2 7 13 7 13s7-7.8 7-13c0-3.9-3.1-7-7-7zm0 9.5A2.5 2.5 0 1 1 12 6.5a2.5 2.5 0 0 1 0 5z"/></svg>
      </span>
      <div><strong>Restwell Clinics</strong>45, Harbour Lane, Fairview - 654321</div>
    </div>

    <div class="contact-item contact-call" style="top:88px">
      <span class="contact-icon">
        <svg width="16" height="16" viewBox="0 0 24 24"><path fill="#fff" d="M6.6 10.8c1.4 2.8 3.8 5.1 6.6 6.6l2.2-2.2c.3-.3.7-.4 1-.2 1.1.4 2.3.6 3.6.6.6 0 1 .4 1 1V20c0 .6-.4 1-1 1C10.6 21 3 13.4 3 4c0-.6.4-1 1-1h3.5c.6 0 1 .4 1 1 0 1.3.2 2.5.6 3.6.1.3 0 .7-.2 1z"/></svg>
      </span>
      <div><strong>Call Us :</strong>015-550-0142</div>
    </div>

    <div class="contact-item contact-email" style="top:88px">
      <span class="contact-icon">
        <svg width="16" height="14" viewBox="0 0 24 20"><rect x="1" y="2" width="22" height="16" rx="2" fill="none" stroke="#fff" stroke-width="2"/><path d="M2 4l10 7 10-7" fill="none" stroke="#fff" stroke-width="2"/></svg>
      </span>
      <div><strong>Email Us :</strong><span class="value">info@restwellclinics.com</span></div>
    </div>

    <div class="copyright">© 2017 Restwell Clinics.<br>All Rights Reserved.</div>
  </footer>

</div>
</body>
</html>
```